Home care support

Design a a great and dynamic website for a healthcare business. Our business will be involved in providing care at home for people with disability and the elderly. Below is a link that I found for a company offering similar services in the US. I am looking for something like this .
I have my files - the latest project in here in through through PixelNest
Sample site : https://pinegroveattendants.net/
Target Market(s)
people with disability and elderly seniors who need home care support
Industry/Entity Type
Health
Coding
Coded - Design and coding required
Number of Pages Required
5+ page
Requirements
Must have
- inspirational pictures and designed with the themed logo (files attached)
Nice to have
- This is my sample and should look like this : https://pinegroveattendants.net/

```html
<!DOCTYPE html>
<html lang="en">
<head>
<meta charset="utf-8">
<title>Havenly – Home Care Support</title>
<link href="https://fonts.googleapis.com/css2?family=Raleway:wght@400;600;700;800;900&family=Open+Sans:wght@400;600;700&display=swap" rel="stylesheet">
<style>
:root{
  --blue:#1b72b2;
  --blue-dark:#135a8f;
  --green:#5b9d38;
  --green-dark:#4c8a2d;
  --ink:#1f2a33;
  --text:#555e66;
  --grey-bg:#eef0f2;
  --charcoal:#2d2d2f;
  --navy:#0f2c47;
  --white:#ffffff;
}
*{box-sizing:border-box;margin:0;padding:0}
html,body{width:1200px;height:4300px;overflow:hidden;background:var(--white)}
body{font-family:"Open Sans",Arial,sans-serif;color:var(--text);font-size:15px;position:relative}
h1,h2,h3,h4,.brand{font-family:"Raleway",Arial,sans-serif}
.btn{display:inline-block;background:var(--green);color:#fff;font-weight:600;font-size:14px;padding:11px 22px;border-radius:4px}
section,header,footer{position:relative;width:1200px}

/* header */
.site-header{height:110px;background:#fff;z-index:2}
.topbar{position:absolute;right:0;top:0;width:600px;height:30px;background:var(--blue);color:#fff;font-size:12px;display:flex;align-items:center;justify-content:flex-end;gap:24px;padding-right:40px;clip-path:polygon(30px 0,100% 0,100% 100%,0 100%)}
.topbar .socials{display:flex;gap:6px;margin-right:auto;margin-left:60px}
.topbar .socials span{width:16px;height:16px;border-radius:50%;background:rgba(255,255,255,.85)}
.brand-block{position:absolute;left:110px;top:14px;display:flex;align-items:center;gap:10px}
.brand-mark{width:40px;height:40px;border-radius:50%;background:var(--blue)}
.brand{font-size:26px;font-weight:800;color:var(--blue);letter-spacing:1px}
.main-nav{position:absolute;right:120px;top:56px;display:flex;gap:34px;align-items:center;font-size:15px;color:var(--ink);font-weight:600}
.main-nav .btn{padding:9px 18px;font-size:13px}

/* hero */
.hero{height:520px;background:linear-gradient(90deg,#f3f1ee 0%,#ece7e1 45%,#d9d2ca 100%);z-index:1}
.hero-photo{position:absolute;left:470px;top:0;width:730px;height:520px;background:linear-gradient(120deg,#e9e4de,#cfc6bc 60%,#bdb2a6)}
.hero-copy{position:absolute;left:155px;top:95px;width:460px}
.hero-copy h1{font-size:50px;font-weight:900;line-height:1.1;color:var(--ink)}
.hero-copy p{margin:18px 0 30px;font-size:17px;color:#3d4650;line-height:1.5;width:390px}
.features{position:absolute;left:155px;top:470px;display:flex;gap:14px}
.feature{width:280px;height:250px;background:#fff;padding:30px 26px;box-shadow:0 6px 18px rgba(0,0,0,.1);clip-path:polygon(0 0,100% 0,100% 88%,0 100%)}
.feature.active{background:var(--green);color:#fff;transform:translateY(-20px);height:270px}
.feature svg{width:36px;height:36px}
.feature h3{font-size:21px;font-weight:700;color:var(--ink);margin:16px 0 12px;line-height:1.2}
.feature.active h3{color:#fff}
.feature p{font-size:13px;line-height:1.55}

/* about */
.about{height:560px}
.about-photo{position:absolute;left:200px;top:190px;width:340px;height:340px;border-radius:50%;background:radial-gradient(circle at 50% 45%,#dfe6ec,#a9bccb)}
.about-ring{position:absolute;left:180px;top:170px;width:380px;height:380px}
.about-copy{position:absolute;left:665px;top:210px;width:400px}
.about-copy h2{font-size:42px;font-weight:900;color:var(--ink);margin-bottom:18px}
.about-copy p{font-size:14px;line-height:1.7;margin-bottom:26px}

/* services */
.services{height:720px;background:var(--grey-bg)}
.services h2{position:absolute;top:60px;width:100%;text-align:center;font-size:42px;font-weight:900;color:var(--ink)}
.services .rule{position:absolute;left:540px;top:122px;width:120px;height:3px;background:var(--blue)}
.service-grid{position:absolute;left:155px;top:170px;width:900px;display:grid;grid-template-columns:repeat(3,1fr);gap:30px 30px}
.service{height:240px;padding:22px 22px 0 84px;position:relative}
.service.active{background:var(--green);color:#fff}
.service .ico{position:absolute;left:18px;top:22px;width:52px;height:52px;border-radius:50%;background:var(--blue);display:flex;align-items:center;justify-content:center}
.service.active .ico{background:#fff}
.service h3{font-size:21px;font-weight:700;color:var(--blue);line-height:1.2;margin-bottom:14px}
.service.active h3{color:#fff}
.service p{font-size:13.5px;line-height:1.55}
.service .more{margin-top:14px;width:20px;height:20px;border:1.5px solid currentColor;border-radius:50%}

/* newsletter band */
.band{height:280px;background:var(--green)}
.band h2{position:absolute;left:155px;top:70px;font-size:40px;font-weight:900;color:#fff;line-height:1.1}
.band p{position:absolute;left:155px;top:182px;font-size:15px;color:#fff;font-weight:600}
.subscribe{position:absolute;left:672px;top:75px;width:370px}
.subscribe .field{height:58px;background:#fff;border-radius:4px;display:flex;align-items:center;justify-content:center;color:#777;font-size:14px}
.subscribe .send{margin:16px auto 0;width:260px;height:42px;background:#fff;color:var(--ink);border-radius:4px;font-size:13px;font-weight:600;display:flex;align-items:center;justify-content:center}

/* blog */
.blog{height:640px}
.blog h2{position:absolute;top:66px;width:100%;text-align:center;font-size:42px;font-weight:900;color:var(--blue)}
.blog .rule{position:absolute;left:540px;top:128px;width:120px;height:3px;background:var(--green)}
.posts{position:absolute;left:155px;top:175px;display:flex;gap:18px;align-items:flex-start}
.post{width:288px;height:420px;background:#fff;box-shadow:0 4px 16px rgba(0,0,0,.1)}
.post .thumb{height:180px;background:linear-gradient(135deg,#d7dde2,#aab6c0)}
.post.featured{background:var(--blue);color:#fff;height:440px}
.post.featured .thumb{background:linear-gradient(135deg,#1e6aa4,#135a8f)}
.post .body{padding:20px 22px}
.post .date{font-size:12px;color:#888;margin-bottom:8px}
.post.featured .date{color:#dce9f4}
.post h4{font-size:16px;font-weight:700;color:var(--blue);margin-bottom:10px}
.post.featured h4{color:#fff}
.post p{font-size:14px;line-height:1.55}
.post .btn{margin-top:20px}

/* advice */
.advice{height:560px;background:var(--charcoal)}
.advice h2{position:absolute;left:155px;top:70px;font-size:44px;font-weight:900;color:#fff;line-height:1.1}
.advice-form{position:absolute;left:155px;top:190px;width:430px;display:grid;grid-template-columns:1fr 1fr}
.advice-form .input{height:52px;background:#fff;border:1px solid #cfcfcf;padding:14px 12px;font-size:13px;color:#555}
.advice-form .message{grid-column:1/3;height:98px}
.advice-form .btn{grid-column:1/2;width:130px;margin-top:28px}
.advice-photo{position:absolute;left:740px;top:60px;width:400px;height:400px;border-radius:50%;background:radial-gradient(circle,#e7e2dc,#b7aa9e)}
.advice-ring{position:absolute;left:720px;top:40px;width:440px;height:440px}

/* testimonials */
.testimonials{height:520px;background:#fff}
.testimonials h2{position:absolute;top:70px;width:100%;text-align:center;font-size:42px;font-weight:900;color:var(--blue)}
.testimonials .rule{position:absolute;left:540px;top:132px;width:120px;height:3px;background:var(--green)}
.quotes{position:absolute;left:155px;top:195px;display:flex;gap:70px}
.quote{width:420px;height:200px;background:#fff;box-shadow:0 4px 18px rgba(0,0,0,.12);padding:28px 26px 0 116px;position:relative}
.quote .avatar{position:absolute;left:22px;top:32px;width:76px;height:76px;border-radius:50%;background:linear-gradient(135deg,#d9d4cf,#a89c91);border:3px solid var(--green)}
.quote p{font-size:14px;line-height:1.6;color:#444}
.quote .who{margin-top:16px;font-size:13px;color:#666}
.quote .who b{color:var(--blue)}
.quote svg{position:absolute;right:22px;bottom:22px}
.dots{position:absolute;top:450px;left:0;width:100%;display:flex;justify-content:center;gap:8px}
.dots span{width:9px;height:9px;border-radius:50%;background:#c8ced4}
.dots span.on{background:var(--green)}

/* footer */
.site-footer{height:390px;background:var(--navy);color:#c9d4de}
.foot-brand{position:absolute;left:155px;top:70px;width:220px}
.foot-brand .row{display:flex;align-items:center;gap:10px}
.foot-brand .brand-mark{background:#fff;width:36px;height:36px}
.foot-brand .brand{color:#fff;font-size:22px}
.foot-brand p{margin-top:20px;font-size:12.5px;line-height:1.6}
.foot-col{position:absolute;top:70px}
.foot-col h4{font-size:15px;color:#fff;font-weight:700;margin-bottom:18px}
.foot-col li{list-style:none;font-size:13px;margin-bottom:11px;display:flex;gap:8px;align-items:flex-start}
.foot-map{width:215px;height:150px;background:linear-gradient(135deg,#e4e7ea,#c9cfd5)}
.copyright{position:absolute;left:0;bottom:0;width:100%;height:70px;text-align:center;font-size:12px;border-top:1px solid rgba(255,255,255,.12);padding-top:26px}
</style>
</head>
<body>

<header class="site-header">
  <div class="topbar">
    <div class="socials"><span></span><span></span><span></span><span></span></div>
    <span>12 Larkspur Road, Fairhaven, 4021</span>
    <span>+1 555 - 014 228</span>
  </div>
  <div class="brand-block"><span class="brand-mark"></span><span class="brand">HAVENLY</span></div>
  <nav class="main-nav">
    <span>Home</span><span>About</span><span>Services</span><span>Blog</span><span>Contact</span>
    <span class="btn">Get Started</span>
  </nav>
</header>

<section class="hero">
  <div class="hero-photo" role="img" aria-label="Caregiver sitting with a smiling senior man in a bright living room"></div>
  <div class="hero-copy">
    <h1>THE BEST HOME,<br>CARE SUPPORT<br>LOVE.</h1>
    <p>It is a long established fact that a reader will be distracted by the readable content</p>
    <span class="btn">Click to Now</span>
  </div>
  <div class="features">
    <div class="feature">
      <svg viewBox="0 0 36 36" fill="none" stroke="#1b72b2" stroke-width="2"><circle cx="13" cy="12" r="5"/><circle cx="25" cy="12" r="4"/><path d="M4 30c0-6 4-10 9-10s9 4 9 10M22 20c5 0 10 3 10 9"/></svg>
      <h3>Professional &amp;<br>Friendly Staff</h3>
      <p>It is a long established fact that a reader will be distracted by the readable content.</p>
    </div>
    <div class="feature active">
      <svg viewBox="0 0 36 36" fill="none" stroke="#fff" stroke-width="2"><circle cx="18" cy="18" r="14"/><path d="M18 9v9l6 4"/></svg>
      <h3>24/7<br>Services</h3>
      <p>It is a long established fact that a reader will be distracted by the readable content.</p>
    </div>
    <div class="feature">
      <svg viewBox="0 0 36 36" fill="none" stroke="#1b72b2" stroke-width="2"><path d="M18 31S5 23 5 13a7 7 0 0 1 13-4 7 7 0 0 1 13 4c0 10-13 18-13 18z"/><path d="M11 17h5l2-4 3 7 2-3h3"/></svg>
      <h3>Emergency<br>Services</h3>
      <p>It is a long established fact that a reader will be distracted by the readable content.</p>
    </div>
  </div>
</section>

<section class="about">
  <div class="about-photo" role="img" aria-label="Nurse caring for an elderly woman at home"></div>
  <svg class="about-ring" viewBox="0 0 380 380" fill="none"><path d="M38 248 A162 162 0 0 0 342 248" stroke="#1b72b2" stroke-width="16" stroke-linecap="round"/></svg>
  <div class="about-copy">
    <h2>ABOUT US</h2>
    <p>There are many variations of passages of Lorem Ipsum available, but the majority have suffered alteration in some form, by injected humour, or randomised words which don't look even slightly believable. If you are going to use a passage of Lorem Ipsum, you need</p>
    <span class="btn">Read More</span>
  </div>
</section>

<section class="services">
  <h2>OUR SERVICES</h2>
  <div class="rule"></div>
  <div class="service-grid">
    <div class="service"><div class="ico"><svg width="26" height="26" viewBox="0 0 26 26" fill="none" stroke="#fff" stroke-width="2"><circle cx="9" cy="8" r="4"/><circle cx="18" cy="9" r="3"/><path d="M2 23c0-5 3-8 7-8s7 3 7 8M16 15c4 0 8 2 8 7"/></svg></div><h3>Companion<br>Care</h3><p>There are many variations of passages of Lorem Ipsum available.</p><div class="more"></div></div>
    <div class="service active"><div class="ico"><svg width="26" height="26" viewBox="0 0 26 26" fill="none" stroke="#5b9d38" stroke-width="2"><path d="M3 12 13 4l10 8v10H3z"/><path d="M10 22v-6h6v6"/></svg></div><h3>Light<br>Housekeeping</h3><p>There are many variations of passages of Lorem Ipsum available.</p><div class="more"></div></div>
    <div class="service"><div class="ico"><svg width="26" height="26" viewBox="0 0 26 26" fill="none" stroke="#fff" stroke-width="2"><rect x="2" y="9" width="16" height="10"/><path d="M18 12h4l3 4v3h-7"/><circle cx="7" cy="21" r="2"/><circle cx="20" cy="21" r="2"/><path d="M10 11v6M7 14h6"/></svg></div><h3>Ambulation<br>Assistance</h3><p>There are many variations of passages of Lorem Ipsum available.</p><div class="more"></div></div>
    <div class="service"><div class="ico"><svg width="26" height="26" viewBox="0 0 26 26" fill="none" stroke="#fff" stroke-width="2"><circle cx="13" cy="13" r="10"/><path d="M9 11h.01M17 11h.01M8 16c3 3 7 3 10 0"/></svg></div><h3>Stimulating<br>Activities</h3><p>There are many variations of passages of Lorem Ipsum available.</p><div class="more"></div></div>
    <div class="service"><div class="ico"><svg width="26" height="26" viewBox="0 0 26 26" fill="none" stroke="#fff" stroke-width="2"><path d="M3 15h20a10 8 0 0 1-20 0zM13 5v5M9 7v3M17 7v3"/></svg></div><h3>Meal<br>Preparation</h3><p>There are many variations of passages of Lorem Ipsum available.</p><div class="more"></div></div>
    <div class="service"><div class="ico"><svg width="26" height="26" viewBox="0 0 26 26" fill="none" stroke="#fff" stroke-width="2"><path d="M2 4h4l3 12h12l2-8H7"/><circle cx="10" cy="21" r="2"/><circle cx="19" cy="21" r="2"/></svg></div><h3>Shopping &amp;<br>Errands</h3><p>There are many variations of passages of Lorem Ipsum available.</p><div class="more"></div></div>
  </div>
</section>

<section class="band">
  <h2>WE'VE BEEN THERE,<br>WE UNDERSTAND</h2>
  <p>It is a long established fact that a reader will be distracted</p>
  <div class="subscribe">
    <div class="field">Enter Your Email</div>
    <div class="send">Subscribe Newsletter Now</div>
  </div>
</section>

<section class="blog">
  <h2>BLOG</h2>
  <div class="rule"></div>
  <div class="posts">
    <article class="post"><div class="thumb" role="img" aria-label="Carer talking with an older man at a table"></div><div class="body"><div class="date">March 17, 2022</div><h4>Lorem Ipsum dummy text</h4><p>Many desktop publishing packages and web page editors now</p></div></article>
    <article class="post featured"><div class="thumb" role="img" aria-label="Blue-toned photo of a senior at home"></div><div class="body"><div class="date">March 17, 2022</div><h4>Lorem Ipsum dummy text</h4><p>Many desktop publishing packages and web page editors now</p><span class="btn">Read More</span></div></article>
    <article class="post"><div class="thumb" role="img" aria-label="Nurse helping an elderly woman"></div><div class="body"><div class="date">March 17, 2022</div><h4>Lorem Ipsum dummy text</h4><p>Many desktop publishing packages and web page editors now</p></div></article>
  </div>
</section>

<section class="advice">
  <h2>LOOKING FOR<br>ADVICE</h2>
  <div class="advice-form">
    <div class="input">Name</div><div class="input">Email</div>
    <div class="input">Ph no</div><div class="input">Inquiry</div>
    <div class="input message">Message</div>
    <span class="btn">Submit Now</span>
  </div>
  <div class="advice-photo" role="img" aria-label="Caregiver helping a senior woman exercise with light weights"></div>
  <svg class="advice-ring" viewBox="0 0 440 440" fill="none"><path d="M30 290 A200 200 0 0 0 410 290" stroke="#fff" stroke-width="16" stroke-linecap="round"/></svg>
</section>

<section class="testimonials">
  <h2>CLIENT TESTIMONIAL</h2>
  <div class="rule"></div>
  <div class="quotes">
    <div class="quote"><div class="avatar" role="img" aria-label="Client portrait"></div><p>It is a long established fact that a reader will be distracted by the readable content of a page when layout.</p><div class="who"><b>Liam Porter</b> , Customer</div><svg width="30" height="24" viewBox="0 0 30 24" fill="#5b9d38"><path d="M0 24V12C0 5 4 1 12 0v5c-4 1-6 3-6 7h6v12zM18 24V12c0-7 4-11 12-12v5c-4 1-6 3-6 7h6v12z"/></svg></div>
    <div class="quote"><div class="avatar" role="img" aria-label="Client portrait"></div><p>It is a long established fact that a reader will be distracted by the readable content of a page when layout.</p><div class="who"><b>Liam Porter</b> , Customer</div><svg width="30" height="24" viewBox="0 0 30 24" fill="#5b9d38"><path d="M0 24V12C0 5 4 1 12 0v5c-4 1-6 3-6 7h6v12zM18 24V12c0-7 4-11 12-12v5c-4 1-6 3-6 7h6v12z"/></svg></div>
  </div>
  <div class="dots"><span></span><span class="on"></span><span></span></div>
</section>

<footer class="site-footer">
  <div class="foot-brand">
    <div class="row"><span class="brand-mark"></span><span class="brand">HAVENLY</span></div>
    <p>Caring hands at home, every day. Gentle support for seniors and families nearby.</p>
  </div>
  <div class="foot-col" style="left:410px"><h4>Quick Link</h4><ul><li>Home</li><li>About</li><li>Services</li><li>Blog</li><li>Contact</li></ul></div>
  <div class="foot-col" style="left:560px"><h4>Quick Contact</h4><ul>
    <li><svg width="14" height="14" viewBox="0 0 14 14" fill="none" stroke="#c9d4de" stroke-width="1.4"><rect x="1" y="3" width="12" height="8"/><path d="m1 3 6 5 6-5"/></svg>hello@havenlycare.net</li>
    <li><svg width="14" height="14" viewBox="0 0 14 14" fill="none" stroke="#c9d4de" stroke-width="1.4"><path d="M3 1h3l1 3-2 1a7 7 0 0 0 4 4l1-2 3 1v3a1 1 0 0 1-1 1A11 11 0 0 1 2 2a1 1 0 0 1 1-1z"/></svg>(555)013-7742-210</li>
    <li><svg width="14" height="14" viewBox="0 0 14 14" fill="none" stroke="#c9d4de" stroke-width="1.4"><path d="M7 13S2 8 2 5a5 5 0 0 1 10 0c0 3-5 8-5 8z"/><circle cx="7" cy="5" r="1.6"/></svg>Elm Row 48, Unit 3, Fairhaven,<br>4021-0087</li>
  </ul></div>
  <div class="foot-col" style="left:830px"><h4>Location</h4><div class="foot-map" role="img" aria-label="Street map of the office location"></div></div>
  <div class="copyright">Copyright@2022 HAVENLY HOMECARE , All Rights Reserved</div>
</footer>

</body>
</html>
```